website re-design

require to re design my existing website ( www.norvelcastline.com ) to show a corporate image of the company . i also require an advise on the content editorial text . i am currently using hostaroo for domain registration and website design and publishing .

Target Market(s)

focus on the meddle east market , but visible for worldwide business opportunity

Industry/Entity Type

It Company

Coding

Coded - Design and coding required

Number of Pages Required

5+ page

Requirements
Must have
• --show the brand color when possible ,
• --professional website reflecting the following main key areas :broadcast /media/consultancy services/technology
• --number of pages to be maintained or increased if necessary
• --adaptive design for all PC and mobiles
• --simple to navigate and get the idea quickly
• --landing page with full image and slight movement in the background
Nice to have
• any interactivity with visitors
• font style to be recommended by the designer ( professional test , easy to read )
• more descriptive image and less text
• visitor to know what we do more from graphics , image and video
• landing page to have some motions ( similar to www.quarrytelm.com/ )

```html
<!DOCTYPE html>
<html lang="en">
<head>
<meta charset="utf-8">
<title>Norvel Castline</title>
<link href="https://fonts.googleapis.com/css2?family=Open+Sans:wght@400;600;700&display=swap" rel="stylesheet">
<style>
:root{
  --orange:#f26b0f;
  --ink:#222;
  --text:#666;
  --grey:#e9e9e9;
  --light:#f4f4f4;
  --black:#0d0d0d;
  --white:#fff;
}
*{box-sizing:border-box;margin:0;padding:0}
html,body{width:1200px;height:3732px;overflow:hidden}
body{font-family:"Open Sans",Arial,sans-serif;color:var(--text);background:var(--white);position:relative}
section,header,footer,nav{position:absolute;left:0;width:1200px}
.brand{display:flex;align-items:center;gap:12px;font-weight:700;font-size:26px;color:var(--ink);text-transform:uppercase;letter-spacing:1px}
.brand-square{width:56px;height:56px;background:var(--orange)}
.site-header{top:0;height:156px}
.site-header .brand{position:absolute;left:40px;top:42px}
.call{position:absolute;right:40px;top:56px;font-size:22px;color:var(--orange);display:flex;align-items:center;gap:12px}
.call b{color:var(--ink);font-weight:600}
.social{position:absolute;right:40px;top:100px;display:flex;gap:10px}
.social span{width:30px;height:30px;border-radius:50%;background:#ccc}
.main-nav{top:156px;height:46px;background:var(--orange);display:flex;padding-left:80px}
.main-nav a{color:var(--white);font-size:15px;font-weight:600;text-decoration:none;padding:0 26px;line-height:46px;text-transform:uppercase}
.main-nav a.active{background:var(--black)}
.hero{top:202px;height:578px;background:linear-gradient(160deg,#3b3e44 0%,#1f2227 45%,#4a4d52 75%,#2a2c30 100%);text-align:center}
.hero h1{position:absolute;top:430px;width:100%;color:var(--white);font-size:50px;font-weight:700;letter-spacing:2px}
.hero p{position:absolute;top:500px;width:100%;color:var(--white);font-size:22px}
.btn{display:inline-block;background:var(--orange);color:var(--white);font-weight:600;font-size:15px;text-transform:uppercase;padding:12px 26px;letter-spacing:.5px}
.hero .btn{position:absolute;top:540px;left:50%;transform:translateX(-50%)}
h2{font-size:44px;font-weight:600;color:var(--ink);text-transform:uppercase;text-align:center}
h2 span{color:var(--orange)}
.lead{font-size:14px;line-height:1.6;text-align:center}
.welcome{top:780px;height:560px;background:var(--light)}
.welcome h2{margin-top:40px}
.welcome .lead{width:960px;margin:22px auto 0}
.areas{display:flex;justify-content:center;gap:70px;margin-top:50px}
.area{width:200px;text-align:center}
.area svg{width:60px;height:60px}
.area h3{color:var(--orange);font-size:22px;font-weight:400;margin:14px 0 10px}
.area p{font-size:14px;line-height:1.5}
.welcome .btn{position:absolute;top:466px;left:50%;transform:translateX(-50%)}
.about{top:1340px;height:380px}
.about h2{text-align:left;position:absolute;left:80px;top:40px}
.about p{position:absolute;left:80px;top:120px;width:740px;font-size:14px;line-height:1.65}
.about .btn{position:absolute;left:80px;top:290px}
.about-mark{position:absolute;left:880px;top:70px;width:200px;height:200px;background:var(--orange)}
.about-name{position:absolute;left:880px;top:286px;font-size:22px;font-weight:700;color:var(--ink);text-transform:uppercase}
.services{top:1720px;height:640px;background:var(--grey)}
.services h2{margin-top:60px}
.services .lead{width:820px;margin:18px auto 0}
.service-list{display:flex;justify-content:center;gap:50px;margin-top:40px}
.service{width:230px;text-align:center}
.service .circle{width:128px;height:128px;border-radius:50%;background:var(--orange);margin:0 auto;display:flex;align-items:center;justify-content:center}
.service .circle svg{width:60px;height:60px}
.service h3{color:var(--ink);font-size:22px;font-weight:400;margin:18px 0 10px;line-height:1.2}
.service p{font-size:14px;line-height:1.5}
.services .btn{position:absolute;top:560px;left:50%;transform:translateX(-50%)}
.solutions{top:2360px;height:360px}
.solutions-visual{position:absolute;left:160px;top:40px;width:260px;height:270px;background:linear-gradient(135deg,#1c3f7a,#4c7fc4 50%,#2b2b2b);}
.solutions h2{position:absolute;left:580px;top:40px;text-align:left}
.solutions p{position:absolute;left:580px;top:110px;width:540px;font-size:14px;line-height:1.6}
.solutions .btn{position:absolute;left:580px;top:260px}
.partners{top:2720px;height:150px;background:#f0f0f0;display:flex;align-items:center;justify-content:space-around;padding:0 40px}
.partners span{width:170px;height:90px;background:#d4d4d4}
.partners span:nth-child(2),.partners span:nth-child(3){border-radius:50%;width:100px;height:100px}
.partners span:nth-child(4){background:#a9cf3a}
.contact{top:2870px;height:340px}
.contact h2{margin-top:50px}
.field{position:absolute;left:120px;width:310px;height:40px;border:1px solid #ddd;font-size:13px;color:#aaa;padding:10px 14px;background:var(--white)}
.message{position:absolute;left:460px;top:160px;width:620px;height:90px;border:1px solid #ddd;background:#f5f5f5;font-size:13px;color:#aaa;padding:10px 14px}
.submit{position:absolute;left:460px;top:260px;width:620px;height:40px;background:var(--orange);color:var(--white);text-align:center;line-height:40px;font-weight:600;font-size:15px}
.employment{top:3210px;height:130px;background:#e3e3e3}
.employment .mark{position:absolute;left:0;top:0;width:236px;height:130px;background:var(--orange);display:flex;align-items:center;justify-content:center;color:var(--white);font-weight:700;font-size:20px;text-transform:uppercase;text-align:center;line-height:1.2}
.employment h3{position:absolute;left:300px;top:22px;color:var(--orange);font-size:30px;font-weight:600}
.employment p{position:absolute;left:300px;top:74px;font-size:18px;color:var(--ink);display:flex;align-items:center;gap:12px}
.employment p b{color:var(--orange);font-weight:400;font-size:22px}
.employment .btn{position:absolute;right:80px;top:42px;background:var(--white);color:var(--orange);border:2px solid var(--orange)}
.site-footer{top:3340px;height:360px;background:var(--black);color:#bbb}
.footer-col{position:absolute;top:60px;font-size:14px;line-height:1.6}
.footer-col h4{color:var(--orange);font-weight:400;font-size:20px;margin-bottom:14px}
.footer-brand .brand{color:var(--white);font-size:20px}
.footer-brand p{margin-top:20px;width:210px}
.footer-col ul{list-style:none}
.post{display:flex;gap:10px;margin-bottom:18px;width:270px}
.post .thumb{width:56px;height:56px;background:linear-gradient(135deg,#555,#999);flex:none}
.post small{display:block;font-size:12px;color:#888}
.touch li{display:flex;gap:10px;align-items:flex-start;margin-bottom:10px}
.touch svg{flex:none;margin-top:4px}
.footer-social{display:flex;gap:14px;margin-top:14px}
.footer-social span{width:36px;height:36px;border-radius:50%;background:var(--orange)}
.copyright{top:3700px;height:32px;background:var(--orange);color:var(--white);font-size:13px;text-align:center;line-height:32px}
</style>
</head>
<body>

<header class="site-header">
  <div class="brand"><span class="brand-square"></span>Norvel Castline</div>
  <div class="call">Call Us Now
    <svg width="20" height="20" viewBox="0 0 24 24"><path fill="#f26b0f" d="M6.6 10.8a15 15 0 0 0 6.6 6.6l2.2-2.2c.3-.3.7-.4 1-.2 1.1.4 2.3.6 3.6.6.6 0 1 .4 1 1V20c0 .6-.4 1-1 1A17 17 0 0 1 3 4c0-.6.4-1 1-1h3.5c.6 0 1 .4 1 1 0 1.3.2 2.5.6 3.6.1.3 0 .7-.2 1z"/></svg>
    <b>+971 4 5550187</b></div>
  <div class="social"><span></span><span></span><span></span><span></span></div>
</header>

<nav class="main-nav">
  <a class="active">Home</a><a>About</a><a>Services</a><a>Solutions</a><a>Customer</a><a>Employment</a><a>Contact</a>
</nav>

<section class="hero" role="img" aria-label="Broadcast studio with cameras on tripods and lighting rigs">
  <h1>NORVEL CASTLINE</h1>
  <p>Broadcast and media solutions</p>
  <span class="btn">Contact Us Now</span>
</section>

<section class="welcome">
  <h2>Welcome to <span>Norvel Castline</span></h2>
  <p class="lead">Norvel Castline provides broadcast system solutions and services to support broadcasters, production houses, telecom and satellite operators in their growth plans, delivering innovation and operation efficiency through strategic planning and smart investment relying on innovative technologies, solutions and professional services.</p>
  <div class="areas">
    <div class="area">
      <svg viewBox="0 0 60 60" fill="none" stroke="#f26b0f" stroke-width="3"><circle cx="30" cy="22" r="4" fill="#f26b0f"/><path d="M30 26 20 56M30 26l10 30M23 46h14"/><path d="M20 12a14 14 0 0 0 0 20M40 12a14 14 0 0 1 0 20M14 6a22 22 0 0 0 0 32M46 6a22 22 0 0 1 0 32"/></svg>
      <h3>Broadcast</h3><p>Studio and transmission systems for stations of any size.</p>
    </div>
    <div class="area">
      <svg viewBox="0 0 60 60" fill="none" stroke="#f26b0f" stroke-width="3"><rect x="6" y="10" width="48" height="32" rx="2"/><path d="M22 52h16M30 42v10"/><path d="M25 19v14l12-7z" fill="#f26b0f"/></svg>
      <h3>Media</h3><p>Content workflows for storage, playout and delivery.</p>
    </div>
    <div class="area">
      <svg viewBox="0 0 60 60" fill="none" stroke="#f26b0f" stroke-width="3"><rect x="4" y="8" width="32" height="22" rx="3"/><path d="M12 30v8l8-8"/><rect x="24" y="26" width="32" height="20" rx="3"/><path d="M48 46v8l-8-8"/></svg>
      <h3>Consultancy Services</h3><p>Planning and advice for projects and investments.</p>
    </div>
    <div class="area">
      <svg viewBox="0 0 60 60" fill="none" stroke="#f26b0f" stroke-width="3"><circle cx="24" cy="34" r="8"/><path d="M24 16v6M24 46v6M6 34h6M36 34h6M11 21l4 4M33 43l4 4M11 47l4-4M33 25l4-4"/><circle cx="46" cy="14" r="5"/><path d="M46 4v4M46 20v4M36 14h4M52 14h4"/></svg>
      <h3>Technology</h3><p>Modern systems built on proven, open platforms.</p>
    </div>
  </div>
  <span class="btn">Know More &#187;</span>
</section>

<section class="about">
  <h2>About <span>Norvel Castline</span></h2>
  <p>Norvel Castline is a technology solution and service provider to the broadcast and telecom media industry. Our objective is to support broadcasters, production houses and telecom operators in their migration plan and developing new concepts and ideas that provide an added value to the channel operation, relying on cutting-edge technology. Our team represents a number of expert and professional engineers with over twenty years of experience in the field.</p>
  <span class="btn">Read More &#187;</span>
  <div class="about-mark"></div>
  <div class="about-name">Norvel Castline</div>
</section>

<section class="services">
  <h2>Our <span>Services</span></h2>
  <p class="lead">We understand the media and entertainment industry and can help guide you through the technology change. We have extensive and varied experience and practice in the broadcast field.</p>
  <div class="service-list">
    <div class="service"><div class="circle"><svg viewBox="0 0 60 60" fill="none" stroke="#fff" stroke-width="3"><rect x="8" y="18" width="32" height="24" rx="3"/><path d="M40 26l12-6v20l-12-6z"/><path d="M16 42l-6 12M32 42l6 12"/></svg></div>
      <h3>Studio and Broadcast Facility Design</h3><p>Full studio layouts from concept to handover.</p></div>
    <div class="service"><div class="circle"><svg viewBox="0 0 60 60" fill="none" stroke="#fff" stroke-width="3"><path d="M8 52h44M14 52V34M26 52V24M38 52V30M50 52V14"/></svg></div>
      <h3>Technology Budget Development</h3><p>Clear cost plans for equipment and upgrades.</p></div>
    <div class="service"><div class="circle"><svg viewBox="0 0 60 60" fill="none" stroke="#fff" stroke-width="3"><rect x="12" y="10" width="36" height="44" rx="3"/><path d="M20 22h20M20 32h20M20 42h12"/></svg></div>
      <h3>Program / Project Management</h3><p>Delivery on time with steady site supervision.</p></div>
    <div class="service"><div class="circle"><svg viewBox="0 0 60 60" fill="none" stroke="#fff" stroke-width="3"><rect x="22" y="6" width="16" height="12"/><rect x="4" y="42" width="16" height="12"/><rect x="22" y="42" width="16" height="12"/><rect x="40" y="42" width="16" height="12"/><path d="M30 18v24M12 42V30h36v12"/></svg></div>
      <h3>System integration</h3><p>Systems joined and tested as one working chain.</p></div>
  </div>
  <span class="btn">View All &#187;</span>
</section>

<section class="solutions">
  <div class="solutions-visual" role="img" aria-label="Video wall of monitors showing broadcast channels"></div>
  <h2>Our <span>Solutions</span></h2>
  <p>Our goal is to provide creative and competitive technology solutions that enable you to grow your business in a cost effective way and in line with your business strategy. Our solutions cover the following categories: newsroom and production systems, playout for TV and radio, digital and online media distribution and contribution.</p>
  <span class="btn">Read More &#187;</span>
</section>

<section class="partners" aria-label="Partners">
  <span></span><span></span><span></span><span></span>
</section>

<section class="contact">
  <h2>Contact <span>Us</span></h2>
  <div class="field" style="top:160px">Name</div>
  <div class="field" style="top:210px">Email</div>
  <div class="field" style="top:260px">Subject</div>
  <div class="message">Message</div>
  <div class="submit">SUBMIT</div>
</section>

<section class="employment">
  <div class="mark">Norvel<br>Castline</div>
  <h3>EMPLOYMENT</h3>
  <p>Send your CV to
    <svg width="22" height="16" viewBox="0 0 22 16" fill="none" stroke="#f26b0f" stroke-width="2"><rect x="1" y="1" width="20" height="14"/><path d="M1 1l10 8 10-8"/></svg>
    <b>info@norvelcastline.com</b></p>
  <span class="btn">Join Us</span>
</section>

<footer class="site-footer">
  <div class="footer-col footer-brand" style="left:80px">
    <div class="brand"><span class="brand-square"></span>Norvel Castline</div>
    <p>Broadcast, media and technology partner for the region and beyond.</p>
  </div>
  <div class="footer-col" style="left:340px">
    <h4>Useful Links</h4>
    <ul><li>Home</li><li>About</li><li>Services</li><li>Solutions</li><li>Customer</li><li>Employment</li><li>Contact</li></ul>
  </div>
  <div class="footer-col" style="left:560px">
    <h4>Latest Blog</h4>
    <div class="post"><div class="thumb" role="img" aria-label="Blog thumbnail"></div><div>Storage trends: exploring objects and cloud<small>7th November, 2016</small></div></div>
    <div class="post"><div class="thumb" role="img" aria-label="Blog thumbnail"></div><div>Q&amp;A: a chief engineer on live studio upgrades<small>7th November, 2016</small></div></div>
  </div>
  <div class="footer-col touch" style="left:880px">
    <h4>Get In Touch With Us</h4>
    <ul>
      <li><svg width="14" height="18" viewBox="0 0 14 18"><path fill="#f26b0f" d="M7 0a7 7 0 0 0-7 7c0 5 7 11 7 11s7-6 7-11a7 7 0 0 0-7-7zm0 10a3 3 0 1 1 0-6 3 3 0 0 1 0 6z"/></svg><span>Bay Studio Quarter<br>Block 2, 2nd Floor</span></li>
      <li><svg width="14" height="14" viewBox="0 0 24 24"><path fill="#f26b0f" d="M6.6 10.8a15 15 0 0 0 6.6 6.6l2.2-2.2c.3-.3.7-.4 1-.2 1.1.4 2.3.6 3.6.6.6 0 1 .4 1 1V20c0 .6-.4 1-1 1A17 17 0 0 1 3 4c0-.6.4-1 1-1h3.5c.6 0 1 .4 1 1 0 1.3.2 2.5.6 3.6.1.3 0 .7-.2 1z"/></svg><span>+971 4 5550187</span></li>
      <li><svg width="14" height="12" viewBox="0 0 22 16" fill="none" stroke="#f26b0f" stroke-width="2"><rect x="1" y="1" width="20" height="14"/><path d="M1 1l10 8 10-8"/></svg><span>info@norvelcastline.com</span></li>
    </ul>
    <div class="footer-social"><span></span><span></span><span></span></div>
  </div>
</footer>

<div class="copyright" style="position:absolute;left:0;width:1200px">&copy; NORVEL CASTLINE - 2016, All Rights Reserved.</div>

</body>
</html>
```